bramblecrest paving card makeover

were a excavation/paving contractor from Monterey ca, I'm looking to have a card designed front and back that has company details on the front and a list of the services we offer on the back.

Target Market(s)

home owners property management companies

Industry/Entity Type

Contractor

Contact Information for Business Card

bramblecrest paving 418 larkmoor st Monterey ca. licensed, insured and bonded
lic#657920 gerald pinsky operations manager

Font styles to use
Serif
Sans Serif

Colors
f78f20

Requirements
Must have
• a list of my services on back, asphalt construction and maintenance, drainage, foundations, retaining walls, chip seals, excavation, grading, landscape ground work, interlocking paver, hydro-seeding, structured and driveway demolition, utility trenching and stump removal.
Nice to have
• my new domain and page address I'm acquiring from pixel bazaar.

```html
<!DOCTYPE html>
<html lang="en">
<head>
<meta charset="utf-8">
<title>Bramblecrest Paving – Business Card</title>
<link href="https://fonts.googleapis.com/css2?family=Roboto:wght@400;500;700&family=Roboto+Condensed:wght@700&display=swap" rel="stylesheet">
<style>
  :root{
    --bg:#4a4a4c;
    --card:#272729;
    --orange:#f78f20;
    --white:#f4f4f4;
    --ink:#141414;
  }
  *{box-sizing:border-box;margin:0;padding:0}
  html,body{width:799px;height:1200px;overflow:hidden}
  body{background:var(--bg);font-family:'Roboto',sans-serif;position:relative}
  .card{position:absolute;left:80px;width:640px;height:366px;background:var(--card);border-radius:26px;overflow:hidden;box-shadow:0 12px 30px rgba(0,0,0,.35)}
  .card--services{top:110px}
  .card--contact{top:690px}

  .brand{position:absolute;display:flex;align-items:center;gap:10px;color:var(--white);font-weight:700;font-size:19px;letter-spacing:.5px;text-transform:uppercase}
  .brand__dot{width:14px;height:14px;border-radius:50%;background:var(--orange);flex:none}

  .card--services .brand{left:34px;top:140px}
  .services{position:absolute;left:312px;top:88px;list-style:none;color:var(--white);font-size:18px;line-height:23px}
  .services li::before{content:"»";color:var(--orange);font-weight:700;margin-right:6px}
  .services .pair::before{content:none}
  .services .pair span::before{content:"»";color:var(--orange);font-weight:700;margin-right:6px}
  .services .pair span+span{margin-left:10px}

  .band{position:absolute;left:0;top:150px;width:100%;height:216px;background:var(--orange)}
  .strip{position:absolute;left:0;bottom:0;width:330px;height:62px;background:var(--card)}
  .card--contact .brand{left:236px;top:84px}
  .contact{position:absolute;left:28px;top:166px;list-style:none;color:var(--ink);font-size:16px;line-height:24px}
  .contact li{display:flex;align-items:center;gap:10px}
  .contact svg{width:13px;height:13px;fill:var(--ink);flex:none}
  .tagline{position:absolute;left:34px;bottom:20px;color:var(--white);font-size:16px;letter-spacing:2px}
  .company{position:absolute;right:34px;top:258px;text-align:right;color:var(--ink)}
  .company__name{font-family:'Roboto Condensed',sans-serif;font-weight:700;font-size:28px}
  .company__lic{font-size:18px;margin-top:4px}
</style>
</head>
<body>

<section class="card card--services" aria-label="Services side">
  <div class="brand"><span class="brand__dot"></span>Bramblecrest Paving</div>
  <ul class="services">
    <li class="pair"><span>Grading</span><span>Drainage</span></li>
    <li class="pair"><span>Hydro-seeding</span><span>Foundations</span></li>
    <li class="pair"><span>Retaining Walls</span><span>Chip Seals</span></li>
    <li class="pair"><span>Excavation</span><span>Interlocking Paver</span></li>
    <li>Landscape Ground Work</li>
    <li>Asphalt Construction &amp; Maintenance</li>
    <li>Structured &amp; Driveway Demolition</li>
    <li>Utility Trenching &amp; Stump Removal</li>
  </ul>
</section>

<section class="card card--contact" aria-label="Contact side">
  <div class="band"></div>
  <div class="strip"></div>
  <div class="brand"><span class="brand__dot"></span>Bramblecrest Paving</div>
  <ul class="contact">
    <li><svg viewBox="0 0 16 16"><path d="M3 1h3l1.5 4-2 1.2a9 9 0 0 0 4.3 4.3L11 8.5l4 1.5v3a2 2 0 0 1-2 2A12 12 0 0 1 1 3a2 2 0 0 1 2-2z"/></svg>(555) 204 7731</li>
    <li><svg viewBox="0 0 16 16"><path d="M1 3h14v10H1z M1 3l7 6 7-6" fill="none" stroke="#141414" stroke-width="1.8"/></svg>info@bramblecrestpaving.com</li>
    <li><svg viewBox="0 0 16 16"><circle cx="8" cy="8" r="6.5" fill="none" stroke="#141414" stroke-width="1.6"/><path d="M1.5 8h13M8 1.5c-3 3.5-3 9.5 0 13M8 1.5c3 3.5 3 9.5 0 13" fill="none" stroke="#141414" stroke-width="1.2"/></svg>www.bramblecrestpaving.com</li>
    <li><svg viewBox="0 0 16 16"><path d="M8 0a5.5 5.5 0 0 0-5.5 5.5C2.5 10 8 16 8 16s5.5-6 5.5-10.5A5.5 5.5 0 0 0 8 0zm0 8a2.5 2.5 0 1 1 0-5 2.5 2.5 0 0 1 0 5z"/></svg>418 larkmoor ST Monterey CA</li>
  </ul>
  <p class="tagline">Licensed, Insured &amp; Bonded</p>
  <div class="company">
    <p class="company__name">Bramblecrest Paving</p>
    <p class="company__lic">Lic # 657920</p>
  </div>
</section>

</body>
</html>
```